Tavenored Crest

Need very crisp business cards for Tavenor Crest per the logo attached. The vision of Tavenor Crest is 'Steer every Venture to Tavenor'. I am going into Freelance | Consulting | Contracting and need this communicated on the card. I need the card to provide a clear message of professionalism and what the vision emulates. Will need an area for my website, LinkedIn, Twitter, as fell as the obvious Name, Address, phone, email... on the back, I would like the Vision but receptive to your design ideas.

```html
<!DOCTYPE html>
<html lang="en">
<head>
<meta charset="utf-8">
<title>Tavenor Crest – Business Cards</title>
<link href="https://fonts.googleapis.com/css2?family=Questrial&display=swap" rel="stylesheet">
<style>
  :root {
    --backdrop: #d9d9d9;
    --card: #f4f4f2;
    --navy: #0e2f6e;
    --ink: #2e2e2e;
    --faint: #c3cfdc;
    --white: #ffffff;
  }
  * { margin: 0; padding: 0; box-sizing: border-box; }
  html, body { width: 1200px; height: 889px; overflow: hidden; }
  body {
    background: var(--backdrop);
    font-family: "Questrial", "Century Gothic", sans-serif;
    color: var(--ink);
    display: flex;
    align-items: center;
    justify-content: center;
    gap: 48px;
  }
  .card {
    position: relative;
    width: 540px;
    height: 309px;
    background: var(--card);
    box-shadow: 0 6px 18px rgba(0,0,0,0.18);
    overflow: hidden;
  }

  /* Front */
  .wordmark {
    color: var(--navy);
    letter-spacing: 0.3px;
    white-space: nowrap;
  }
  .card-front .wordmark { position: absolute; left: 36px; top: 30px; font-size: 26px; }
  .vision-block {
    position: absolute;
    right: 28px;
    top: 78px;
    width: 236px;
    text-align: center;
  }
  .vision-mark {
    color: var(--faint);
    font-size: 28px;
    line-height: 1.1;
    white-space: nowrap;
    margin-bottom: 12px;
  }
  .vision-text { font-size: 12px; color: var(--ink); letter-spacing: 0.3px; }
  .holder { position: absolute; left: 40px; top: 128px; }
  .holder-name { font-size: 19px; color: var(--ink); }
  .holder-position { font-size: 12px; color: var(--navy); font-style: italic; margin-top: 2px; }
  .contacts { position: absolute; left: 44px; top: 212px; list-style: none; }
  .contacts li {
    display: flex;
    align-items: center;
    gap: 7px;
    font-size: 13px;
    line-height: 20px;
  }
  .contact-icon { width: 13px; height: 13px; flex: none; }

  /* Back */
  .services {
    position: absolute;
    top: 30px;
    width: 100%;
    text-align: center;
    font-size: 15px;
    letter-spacing: 0.4px;
  }
  .services .divider { color: var(--navy); margin: 0 5px; }
  .card-back .wordmark {
    position: absolute;
    top: 110px;
    width: 100%;
    text-align: center;
    font-size: 38px;
  }
  .contact-band {
    position: absolute;
    left: 0; right: 0; bottom: 34px;
    height: 58px;
    background: var(--navy);
    display: flex;
    align-items: center;
    justify-content: space-between;
    padding: 0 26px;
  }
  .website { color: var(--white); font-size: 15px; letter-spacing: 4px; }
  .social-dot {
    width: 16px; height: 16px;
    border-radius: 50%;
    background: var(--white);
    flex: none;
  }
</style>
</head>
<body>

  <section class="card card-front" aria-label="Business card front">
    <div class="wordmark">Tavenored Crest</div>

    <div class="vision-block">
      <p class="vision-mark" aria-hidden="true">Tavenored Crest</p>
      <p class="vision-text">Steer every Venture to Tavenor</p>
    </div>

    <div class="holder">
      <p class="holder-name">Name Surname</p>
      <p class="holder-position">position</p>
    </div>

    <ul class="contacts">
      <li>
        <svg class="contact-icon" viewBox="0 0 14 14" aria-hidden="true">
          <circle cx="7" cy="7" r="7" fill="#0e2f6e"/>
          <path d="M7 3.2a2.4 2.4 0 0 0-2.4 2.4C4.6 7.4 7 10.6 7 10.6s2.4-3.2 2.4-5A2.4 2.4 0 0 0 7 3.2z" fill="#fff"/>
          <circle cx="7" cy="5.6" r="0.9" fill="#0e2f6e"/>
        </svg>
        Address
      </li>
      <li>
        <svg class="contact-icon" viewBox="0 0 14 14" aria-hidden="true">
          <circle cx="7" cy="7" r="7" fill="#0e2f6e"/>
          <path d="M4.6 3.6l1.3-.2.8 1.8-.9.7c.4 1 1.1 1.7 2.1 2.1l.7-.9 1.8.8-.2 1.3c-3.2.3-5.9-2.4-5.6-5.6z" fill="#fff"/>
        </svg>
        +00 123 1234
      </li>
      <li>
        <svg class="contact-icon" viewBox="0 0 14 14" aria-hidden="true">
          <circle cx="7" cy="7" r="7" fill="#0e2f6e"/>
          <circle cx="7" cy="7" r="3.4" fill="none" stroke="#fff" stroke-width="1.2"/>
          <circle cx="7" cy="7" r="1.2" fill="#fff"/>
        </svg>
        email@email.com
      </li>
    </ul>
  </section>

  <section class="card card-back" aria-label="Business card back">
    <p class="services">Freelance<span class="divider">|</span>Consulting<span class="divider">|</span>Contracting</p>

    <div class="wordmark">Tavenored Crest</div>

    <div class="contact-band">
      <span class="social-dot" role="img" aria-label="Professional network profile"></span>
      <span class="website">www.tavenorcrest.com</span>
      <span class="social-dot" role="img" aria-label="Social media profile"></span>
    </div>
  </section>

</body>
</html>
```